Economic Development Consulting needs killer brochure for National Civic Design Society Conference

Brightwater Advisors is an elite sponsor for the NCDS conference this year. Our Three service offerings for the event are
Economic Development Master Planning (and our proprietary approach)
Feasibility Studies and Site Options Analysis (also leverages our proprietary approach)
Resilience Assessment & Planning
Our slogan is Customized consulting for communities and community planners and Uncommon Insights — Aligning Resources to Opportunity

We need a square, trifold brochure, and we would like 3 posters, one dedicated to each of our service offerings, matching the brochure.

The NCDS conference site is http://www.ncdsfrontier.org/annual-conference
Updates

We have increased the budget for the brochure requested. The posters referenced int eh posting will be a separate project, offered to the designer who designs the brochure.

Reason: We are looking at adding some additional text.

Target Market(s)

Planners, Architects,

Industry/Entity Type

Consulting

Font styles to use
Sans Serif

Colors
0255a3

Requirements
Must have
• Square, trifold

```html
<!DOCTYPE html>
<html lang="en">
<head>
<meta charset="utf-8">
<title>Brightwater Advisors – Conference Brochure</title>
<link rel="stylesheet" href="https://fonts.googleapis.com/css2?family=Barlow:wght@300;400;600;700&display=swap">
<style>
:root{
  --page-bg:#d6d6d6;
  --brand-blue:#0255a3;
  --band-blue:#1560aa;
  --heading-gray:#6e7378;
  --body-ink:#1f2a33;
  --white:#ffffff;
}
*{margin:0;padding:0;box-sizing:border-box}
html,body{width:1200px;height:1000px;overflow:hidden}
body{background:var(--page-bg);font-family:"Barlow",Arial,sans-serif;position:relative}
.brochure{position:absolute;left:49px;top:303px;width:1105px;height:368px;box-shadow:3px 4px 6px rgba(0,0,0,.25);background:var(--white);overflow:hidden}
.panel{position:absolute;top:0;width:369px;height:303px}
.panel--economic{left:0}
.panel--feasibility{left:369px;width:368px}
.panel--resilience{left:737px;width:368px}
.visual{position:absolute;left:0;width:100%}
.visual--top{top:0;height:152px}
.visual--bottom{top:152px;height:151px}
.economic-top{background:linear-gradient(120deg,#ffffff 0%,#f3f4f6 55%,#d9dce0 100%)}
.feasibility-top{background:linear-gradient(100deg,#e3e9ef 0%,#eef2f5 55%,#c9ced3 100%)}
.resilience-top{background:linear-gradient(90deg,#f4f5f6 0%,#ffffff 50%,#d5d9dd 100%)}
.economic-bottom{background:linear-gradient(90deg,#f2f4f6 0%,#dfe8ee 30%,#9fc4d6 60%,#cfe3ec 100%)}
.feasibility-bottom{background:linear-gradient(135deg,#f1f1f4 0%,#cfd2de 45%,#7d83a8 75%,#e8e3d4 100%)}
.resilience-bottom{background:linear-gradient(135deg,#6fb3d1 0%,#2f86b0 45%,#5aa4c6 80%,#1f6f98 100%)}
.copy{position:absolute;top:58px;left:26px}
.panel--feasibility .copy{left:27px}
.panel--resilience .copy{left:26px}
.copy__title{font-weight:700;font-size:17px;line-height:18px;color:var(--brand-blue)}
.copy__subtitle{font-weight:300;font-size:20px;line-height:22px;color:var(--heading-gray);letter-spacing:.6px;text-transform:uppercase;margin-bottom:4px}
.copy__list{list-style:none;font-size:10px;line-height:12px;color:var(--body-ink);letter-spacing:.2px}
.copy__list li{padding-left:2px}
.band{position:absolute;left:0;top:303px;width:100%;height:65px;background:var(--band-blue)}
.band__sponsor{position:absolute;left:26px;top:30px;font-size:7.5px;font-weight:600;color:var(--white);letter-spacing:.2px}
.band__slogan{position:absolute;left:401px;top:27px;font-size:11px;font-weight:400;color:#dce8f4;letter-spacing:.3px}
.band__brand{position:absolute;right:20px;top:24px;display:flex;align-items:center;gap:6px}
.band__name{font-size:11px;font-weight:700;color:var(--white);line-height:11px;text-align:right;text-transform:uppercase;letter-spacing:.3px}
.band__mark{width:14px;height:14px;background:var(--white)}
</style>
</head>
<body>
<main class="brochure">
  <section class="panel panel--economic">
    <div class="visual visual--top economic-top" role="img" aria-label="Network of dark spheres joined by lines"></div>
    <div class="visual visual--bottom economic-bottom" role="img" aria-label="Businessman in white shirt and tie in a bright blurred office"></div>
    <div class="copy">
      <h2 class="copy__title">Economic</h2>
      <p class="copy__subtitle">Development</p>
      <ul class="copy__list">
        <li>Award Winning Proprietary Approach</li>
        <li>Culture or Values Based Planning</li>
        <li>Stakeholder Agreement, Community Voice</li>
      </ul>
    </div>
  </section>
  <section class="panel panel--feasibility">
    <div class="visual visual--top feasibility-top" role="img" aria-label="Silver puzzle pieces fitting together"></div>
    <div class="visual visual--bottom feasibility-bottom" role="img" aria-label="Printed bar chart with a pen resting on it"></div>
    <div class="copy">
      <h2 class="copy__title">Feasibility Studies &amp;</h2>
      <p class="copy__subtitle">Site Options Analysis</p>
      <ul class="copy__list">
        <li>Comprehensive analysis of current state and options</li>
        <li>Statistical modeling tool creates best fit scenarios</li>
        <li>Strategic planning for current and future use</li>
      </ul>
    </div>
  </section>
  <section class="panel panel--resilience">
    <div class="visual visual--top resilience-top" role="img" aria-label="Chrome balls of a swinging pendulum"></div>
    <div class="visual visual--bottom resilience-bottom" role="img" aria-label="Blurred people walking on a glass staircase"></div>
    <div class="copy">
      <h2 class="copy__title">Resilience</h2>
      <p class="copy__subtitle">Assessment &amp; Planning</p>
      <ul class="copy__list">
        <li>Instilling the agility to capitalize on opportunities</li>
        <li>Not surviving, but thriving during change</li>
        <li>Building awareness on the fringe</li>
      </ul>
    </div>
  </section>
  <footer class="band">
    <p class="band__sponsor">Brightwater Advisors is proud to be an elite sponsor of the 2014 NCDS Frontier State Conference</p>
    <p class="band__slogan">Customized consulting for communities and community planners</p>
    <div class="band__brand">
      <p class="band__name">Brightwater<br>Advisors</p>
      <span class="band__mark"></span>
    </div>
  </footer>
</main>
</body>
</html>
```